Turn this Powerpoint into a PPT Video / Slidshow

Using PPT Animations/Transitions and adjusting the size of text, text boxes, I'd like help to turn this presentation into something that could be a simple video WITHOUT narration. That means making some of the boxes stand out more with bigger font, using animations, etc. It should be short and simple - nothing too fancy but it should be readable as a video. If you add some appropriate music, great but not necessary.

Adjust to design is allowed as long as it doesn't stray too far from the branding. The font is sometimes small, so it's the words and call-outs that need to be easier to read in a video teaser.

```html
<!DOCTYPE html>
<html lang="en">
<head>
<meta charset="utf-8">
<title>Vaultwise – Intelligent Middleware</title>
<link href="https://fonts.googleapis.com/css2?family=Barlow:wght@400;500;600;700&display=swap" rel="stylesheet">
<style>
  :root {
    --canvas: #000000;
    --hero-dark: #0f1d2a;
    --hero-mid: #1c3347;
    --hero-glow: #2d8fb0;
    --hero-text: #ffffff;
    --band-light: #eef5fc;
    --band-blue: #3a7ea9;
    --brand-purple: #5b2a6e;
    --accent-red: #ef5350;
    --body-bg: #ebebea;
    --body-text: #1b1b1b;
    --header-bg: #f6f6f6;
    --footer-bg: #565656;
    --footer-text: #ffffff;
  }
  * { margin: 0; padding: 0; box-sizing: border-box; }
  html, body {
    width: 1023px; height: 1200px; overflow: hidden;
    background: var(--canvas);
    font-family: "Barlow", Arial, sans-serif;
  }
  .canvas { position: relative; width: 1023px; height: 1200px; }

  /* Title slide */
  .slide-title {
    position: absolute; left: 16px; top: 19px; width: 987px; height: 560px;
    overflow: hidden;
  }
  .hero {
    position: absolute; left: 0; top: 0; width: 100%; height: 380px;
    background:
      radial-gradient(circle at 76% 30%, rgba(45,143,176,0.55) 0, rgba(45,143,176,0) 22%),
      linear-gradient(90deg, var(--hero-dark) 0%, var(--hero-mid) 55%, #23364a 100%);
  }
  .hero-heading {
    position: absolute; left: 101px; top: 140px; color: var(--hero-text);
  }
  .hero-heading h1 {
    font-size: 38px; font-weight: 700; letter-spacing: 0.3px; line-height: 1;
  }
  .hero-heading p {
    margin-top: 14px; font-size: 25px; font-weight: 400; line-height: 34px;
  }
  .brand-band {
    position: absolute; left: 0; top: 380px; width: 100%; height: 158px;
    background: var(--band-light);
    display: flex; align-items: center; justify-content: center; gap: 12px;
  }
  .brand-mark { width: 22px; height: 22px; background: var(--brand-purple); }
  .brand-name {
    font-size: 40px; font-weight: 700; color: var(--brand-purple);
  }
  .accent-band {
    position: absolute; left: 0; bottom: 0; width: 100%; height: 22px;
    background: var(--band-blue);
  }

  /* Content slide */
  .slide-content {
    position: absolute; left: 13px; top: 620px; width: 994px; height: 563px;
    background: var(--body-bg); overflow: hidden;
  }
  .slide-header {
    position: absolute; left: 0; top: 0; width: 100%; height: 90px;
  }
  .slide-header svg { position: absolute; left: 0; top: 0; }
  .slide-header h2 {
    position: absolute; left: 21px; top: 12px;
    font-size: 27px; font-weight: 600; line-height: 32px;
    color: var(--accent-red);
  }
  .header-brand {
    position: absolute; right: 28px; top: 32px;
    font-size: 20px; font-weight: 700; color: var(--brand-purple);
  }
  .point {
    position: absolute; left: 26px; top: 140px; width: 820px;
    display: flex; gap: 12px;
  }
  .point-icon { flex: none; margin-top: 8px; }
  .point-body { color: var(--body-text); font-size: 25px; line-height: 35px; }
  .point-body strong {
    font-size: 38px; font-weight: 700; color: var(--accent-red);
  }
  .point-body p + p { margin-top: 30px; }
  .slide-footer {
    position: absolute; left: 0; bottom: 0; width: 100%; height: 32px;
    background: var(--footer-bg); color: var(--footer-text);
    font-size: 15px; line-height: 32px; padding-left: 13px;
  }
</style>
</head>
<body>
<div class="canvas">

  <section class="slide-title">
    <div class="hero" role="img" aria-label="Photo of a businessman in a suit holding a glass tablet with a glowing digital brain hovering above it"></div>
    <div class="hero-heading">
      <h1>INTRODUCING VAULTWISE</h1>
      <p>Intelligent Middleware for<br>Intelligent Content Management</p>
    </div>
    <div class="brand-band">
      <span class="brand-mark"></span>
      <span class="brand-name">Vaultwise</span>
    </div>
    <div class="accent-band"></div>
  </section>

  <section class="slide-content">
    <header class="slide-header">
      <svg width="994" height="90" viewBox="0 0 994 90">
        <path d="M0 0 H838 L808 84 Q806 90 798 90 H0 Z" fill="#f7f7f7"/>
        <path d="M858 0 H994 V90 H834 Q826 90 829 82 Z" fill="#f3f3f3"/>
        <path d="M0 88 H800" stroke="#d8d8d8" stroke-width="2"/>
      </svg>
      <h2>Surfacing the most relevant content or information<br>at the point of interaction</h2>
      <span class="header-brand">Vaultwise</span>
    </header>

    <div class="point">
      <svg class="point-icon" width="36" height="36" viewBox="0 0 30 30">
        <circle cx="14" cy="16" r="11.5" fill="none" stroke="#ef5350" stroke-width="2.4"/>
        <path d="M8 16 L13 21 L27 5" fill="none" stroke="#ef5350" stroke-width="2.8" stroke-linecap="round" stroke-linejoin="round"/>
      </svg>
      <div class="point-body">
        <p><strong>Surfacing</strong> means suggesting contextually-relevant content or information at the right time, in the right format and the right application relevant to an interaction</p>
        <p>It accomplishes this by tracking previous behavior and interests of a user and her/his network - and then correlating relevant content and information with those interests using Machine Learning and AI techniques</p>
      </div>
    </div>

    <footer class="slide-footer">Copyright text here</footer>
  </section>

</div>
</body>
</html>
```